Shoes & Inserts Postcard Campaign

Hi,
We are looking to send a postcard to our patients reminding them that they may be eligible for shoes and inserts in the new calendar year. The patient demographic is mostly 50 and above.

We plan on uploading the image to Kolbo Press and have them create the postcard for us to be sent out.
Dimensions: 4.2"x5.5"
Front & Back Design
Images should be in high resolution. Entire postcard to be high resolution, if not vector.
I've attached a sample of what we used to have with the dimension parameters and our logo.

Verbiage can be the same, switch it to 2023. Front of the postcard doesn't need our logo. Looking for eye catching. Warm and welcoming.

Thank you,
Tomas Ibe

```html
<!DOCTYPE html>
<html lang="en">
<head>
<meta charset="utf-8">
<title>Shoes &amp; Inserts Postcard</title>
<link href="https://fonts.googleapis.com/css2?family=Poppins:wght@400;500;600;700;800&display=swap" rel="stylesheet">
<style>
:root{
  --bg:#e6e6e6;
  --ink:#262626;
  --dark:#2b2b2b;
  --black:#141414;
  --teal:#55c1a6;
  --orange:#f47b3f;
  --white:#ffffff;
  --line:#cfcfcf;
}
*{box-sizing:border-box;margin:0;padding:0}
html,body{width:1200px;height:2557px;overflow:hidden}
body{background:var(--bg);font-family:"Poppins",sans-serif;position:relative;color:var(--ink)}
.card{position:absolute;left:150px;width:900px;height:686px;background:var(--white);overflow:hidden;box-shadow:0 4px 14px rgba(0,0,0,.25)}
.front{top:470px}
.back{top:1400px}
.abs{position:absolute}

/* front */
.brand{font-weight:800;color:var(--orange);line-height:1.05;letter-spacing:.5px}
.brand-mark{display:inline-block;width:34px;height:34px;border-radius:50%;background:var(--teal);vertical-align:middle;margin-right:14px}
.front .brand{left:48px;top:70px;font-size:36px}
.hero-photo{right:0;top:0;width:440px;height:610px;background:linear-gradient(160deg,#d9d9d9 0%,#6a6a6a 45%,#e97a4c 70%,#3a3a3a 100%);}
.band{left:0;top:188px;width:900px;height:305px;background:radial-gradient(ellipse at 70% 40%,#3a3a3a,var(--dark) 70%)}
.lines{left:0;top:493px;width:900px;height:120px}
.q1{left:48px;top:218px;font-size:38px;font-weight:700;color:var(--white);line-height:1.1}
.q2{left:46px;top:262px;font-size:74px;font-weight:800;color:var(--teal);line-height:1}
.q3{left:44px;top:332px;font-size:74px;font-weight:800;color:var(--orange);line-height:1;white-space:nowrap}
.thumb{top:422px;width:248px;height:135px;border:6px solid var(--dark);border-top-color:var(--teal);box-shadow:0 4px 8px rgba(0,0,0,.35)}
.t1{left:57px;background:linear-gradient(180deg,#9aa49a 0%,#6f756f 55%,#3c3c3c 100%)}
.t2{left:318px;background:linear-gradient(180deg,#fafafa 0%,#eee 55%,#d8b7a4 80%,#f4f4f4 100%);border-top-color:var(--orange)}
.t3{left:581px;background:linear-gradient(180deg,#7f9e62 0%,#c9a87a 50%,#f18a55 70%,#5a5a5a 100%)}
.footer-svg{left:0;top:586px;width:900px;height:100px}
.call{left:48px;top:600px;font-size:32px;font-weight:800;color:var(--ink);white-space:nowrap;display:flex;align-items:center;gap:10px}
.web{left:500px;top:606px;font-size:25px;font-weight:700;color:var(--black);letter-spacing:2px;white-space:nowrap}
.web span{color:var(--orange)}

/* back */
.panel{left:0;top:0;width:476px;height:540px;background:var(--dark)}
.panel-low{left:0;top:540px;width:196px;height:146px;background:var(--dark)}
.stripe-a{left:470px;top:0;width:7px;height:540px;background:var(--teal)}
.stripe-b{left:190px;top:540px;width:7px;height:146px;background:var(--teal)}
.back .brand{left:46px;top:70px;font-size:28px}
.keep{left:46px;top:146px;font-size:48px;font-weight:800;color:var(--white);line-height:1}
.moving{left:46px;top:196px;font-size:48px;font-weight:800;color:var(--teal);line-height:1}
.offer{left:0;top:252px;width:477px;height:128px;background:var(--orange);padding:8px 0 0 52px}
.offer p{font-size:20px;font-weight:500;color:var(--ink);line-height:1.2}
.offer h3{font-size:32px;font-weight:800;color:var(--white);line-height:1;margin-top:6px}
.offer h3 b{color:var(--ink)}
.notes{left:52px;top:390px;font-size:16px;color:var(--white);line-height:1.22}
.notes em{font-style:normal;color:var(--teal)}
.pill{left:46px;top:456px;width:410px;height:30px;border-radius:15px;background:var(--white);display:flex;align-items:center;gap:6px;padding-left:12px;font-size:16px;font-weight:700;color:var(--ink);white-space:nowrap}
.sched{left:46px;top:490px;font-size:16px;font-weight:700;color:var(--orange)}
.addr{left:76px;top:534px;font-size:16px;color:var(--white);line-height:1.2}
.pin{left:46px;top:536px}
.mail{left:510px;top:88px;font-size:20px;color:var(--ink);line-height:1.22}
.stamp{left:720px;top:88px;width:136px;height:137px;border:1.5px solid #9a9a9a}
</style>
</head>
<body>

<section class="card front" aria-label="Postcard front">
  <div class="abs band"></div>
  <svg class="abs lines" viewBox="0 0 900 120" aria-hidden="true">
    <path d="M0 120 L900 0 L900 120 Z" fill="#f3f3f3"/>
    <path d="M420 120 C600 60 750 30 900 10" stroke="var(--line)" fill="none"/>
    <path d="M480 120 C640 70 780 40 900 25" stroke="var(--line)" fill="none"/>
    <path d="M540 120 C690 80 800 55 900 40" stroke="var(--line)" fill="none"/>
  </svg>
  <div class="abs hero-photo" role="img" aria-label="Photo of a walking person's legs in running shoes, one foot glowing orange to show the bones"></div>
  <div class="abs brand"><span class="brand-mark"></span>RIDGEWAY<br>FOOT &amp; ANKLE</div>
  <div class="abs q1">HAVE YOU ORDERED</div>
  <div class="abs q2">THIS YEAR’S</div>
  <div class="abs q3">SHOES AND INSERTS?</div>
  <div class="abs thumb t1" role="img" aria-label="Photo of feet in running shoes walking on a path"></div>
  <div class="abs thumb t2" role="img" aria-label="Photo of a bare foot with an orthotic insert"></div>
  <div class="abs thumb t3" role="img" aria-label="Photo of a runner's foot highlighted in orange in a park"></div>
  <svg class="abs footer-svg" viewBox="0 0 900 100" aria-hidden="true">
    <polygon points="470,54 900,54 900,100 505,100" fill="var(--black)"/>
    <polygon points="0,0 475,0 505,100 0,100" fill="var(--teal)"/>
  </svg>
  <div class="abs call">CALL US
    <svg width="30" height="30" viewBox="0 0 30 30" aria-hidden="true"><circle cx="15" cy="15" r="14" fill="var(--ink)"/><path d="M10 8c1-1 2 0 3 2s0 2-1 3c1 2 3 4 5 5 1-1 1-2 3-1s3 2 2 3c-1 2-3 3-6 1-3-2-6-5-7-8-1-2 0-4 1-5z" fill="var(--white)"/></svg>
    (555)014-0192</div>
  <div class="abs web">www.<span>stridewellfeet</span>.com</div>
</section>

<section class="card back" aria-label="Postcard back">
  <div class="abs panel"></div>
  <div class="abs panel-low"></div>
  <div class="abs stripe-a"></div>
  <div class="abs stripe-b"></div>
  <div class="abs brand"><span class="brand-mark"></span>RIDGEWAY<br>FOOT &amp; ANKLE</div>
  <div class="abs keep">WE KEEP YOU</div>
  <div class="abs moving">MOVING!</div>
  <div class="abs offer">
    <p>We are pleased to inform that you<br>may be eligible for a</p>
    <h3>NEW PAIR OF SHOES<br><b>AND</b> INSERTS!</h3>
  </div>
  <div class="abs notes"><em>*</em>Last day to place a shoe order is <em>10/31/23.*</em><br><em>**</em>If you have received your shoes and<br>inserts for <em>2023</em>, please disregard.<em>**</em></div>
  <div class="abs pill">PLEASE CALL OUR OFFICE
    <svg width="18" height="18" viewBox="0 0 30 30" aria-hidden="true"><circle cx="15" cy="15" r="14" fill="var(--teal)"/><path d="M10 8c1-1 2 0 3 2s0 2-1 3c1 2 3 4 5 5 1-1 1-2 3-1s3 2 2 3c-1 2-3 3-6 1-3-2-6-5-7-8-1-2 0-4 1-5z" fill="var(--white)"/></svg>
    (555)014-0192</div>
  <div class="abs sched">TO SCHEDULE YOUR APPOINTMENT</div>
  <svg class="abs pin" width="20" height="24" viewBox="0 0 20 24" aria-hidden="true"><path d="M10 1a8 8 0 0 0-8 8c0 6 8 14 8 14s8-8 8-14a8 8 0 0 0-8-8z" fill="var(--teal)"/><circle cx="10" cy="9" r="3" fill="var(--dark)"/></svg>
  <div class="abs addr">88 Alder<br>Park<br>Drive,<br>Suite 210<br>Millbrook,<br>MD 20000</div>
  <div class="abs mail">john Smith<br>123 Main Street<br>Small Town,<br>USA 00000-0000</div>
  <div class="abs stamp"></div>
</section>

</body>
</html>
```